Tidewell Grove Vitamin C Serum

We need a product label and box designed for our Vitamin C Serum product. The label will go on a 2oz bottle and the box will hold the 2oz bottle. Attached are the box and label templates as well as a Vitamin C Serum we have with another brand.

For this brand, we're looking to have the product look high end/luxury.

Target Market(s)

40+ year old women

```html
<!DOCTYPE html>
<html lang="en">
<head>
<meta charset="utf-8">
<title>Tidewell Grove Vitamin C Serum – Box and Label</title>
<link href="https://fonts.googleapis.com/css2?family=PT+Serif:wght@700&family=Barlow+Condensed:wght@500;600&display=swap" rel="stylesheet">
<style>
  :root {
    --backdrop: #7d62b8;
    --panel-dark: #2f2f31;
    --panel-edge: #1a1a1b;
    --orange: #e8722a;
    --yellow: #f5cc25;
    --aloe-green: #7cbf3a;
    --aloe-deep: #3f7f24;
    --outline-green: #8fbf3c;
    --lotus-grey: #8a8a8c;
    --lotus-yellow: #f2c21c;
    --white: #ffffff;
    --ink: #2a2a2a;
  }
  * { box-sizing: border-box; margin: 0; padding: 0; }
  html, body { width: 1200px; height: 789px; overflow: hidden; }
  body { background: var(--backdrop); position: relative; font-family: "Barlow Condensed", sans-serif; }

  .box-front, .bottle-label {
    position: absolute;
    background: var(--panel-dark);
    overflow: hidden;
    box-shadow: 0 0 0 1px var(--panel-edge);
  }
  .box-front { left: 330px; top: 15px; width: 300px; height: 760px; }
  .bottle-label { left: 720px; top: 165px; width: 320px; height: 460px; }

  .top-band { position: absolute; left: 0; top: 0; width: 100%; height: 70px; background: var(--orange); }

  .brand { position: absolute; left: 0; width: 100%; display: flex; align-items: center; justify-content: center; gap: 8px; color: var(--white); font-weight: 600; letter-spacing: 1px; text-transform: uppercase; }
  .brand-dot { border-radius: 50%; background: var(--orange); }
  .box-front .brand { top: 110px; font-size: 26px; }
  .box-front .brand-dot { width: 18px; height: 18px; }
  .bottle-label .brand { top: 48px; font-size: 20px; }
  .bottle-label .brand-dot { width: 14px; height: 14px; }

  .product-name {
    position: absolute; left: 0; width: 100%;
    text-align: center;
    font-family: "PT Serif", serif; font-weight: 700;
    color: var(--white);
    line-height: 1.1;
  }
  .box-front .product-name { top: 250px; font-size: 40px; }
  .bottle-label .product-name { top: 130px; font-size: 26px; }

  .facial-pill { position: absolute; left: 50%; transform: translateX(-50%); background: var(--yellow); color: var(--ink); border-radius: 6px; text-align: center; font-weight: 500; letter-spacing: 0.5px; }
  .box-front .facial-pill { top: 428px; width: 200px; height: 42px; line-height: 42px; font-size: 22px; }
  .bottle-label .facial-pill { top: 248px; width: 140px; height: 28px; line-height: 28px; font-size: 15px; }

  .aloe-art { position: absolute; left: 50%; transform: translateX(-50%); background: radial-gradient(ellipse at 50% 80%, var(--aloe-green), var(--aloe-deep) 60%, transparent 75%); }
  .box-front .aloe-art { top: 485px; width: 170px; height: 95px; }
  .bottle-label .aloe-art { top: 285px; width: 110px; height: 60px; }

  .ingredient-box { position: absolute; left: 50%; transform: translateX(-50%); border: 1.5px solid var(--outline-green); color: var(--outline-green); text-align: center; font-weight: 500; line-height: 1; }
  .box-front .ingredient-box { top: 584px; width: 200px; padding: 5px 0; font-size: 20px; }
  .bottle-label .ingredient-box { top: 350px; width: 110px; padding: 3px 0; font-size: 12px; }

  .tagline { position: absolute; left: 0; width: 100%; text-align: center; color: var(--orange); font-weight: 600; }
  .box-front .tagline { top: 642px; font-size: 22px; }
  .bottle-label .tagline { top: 390px; font-size: 13px; }

  .lotus-art { position: absolute; left: 50%; transform: translateX(-50%); border-radius: 50% 50% 0 0 / 100% 100% 0 0; }
  .box-front .lotus-art { bottom: 0; width: 250px; height: 80px; background: var(--lotus-grey); }
  .bottle-label .lotus-art { bottom: 0; width: 90px; height: 42px; background: var(--lotus-yellow); }

  .volume { position: absolute; left: 0; width: 100%; text-align: center; font-family: Arial, sans-serif; color: var(--white); }
  .box-front .volume { bottom: 22px; font-size: 15px; }
  .bottle-label .volume { bottom: 10px; font-size: 9px; color: var(--ink); }
</style>
</head>
<body>

<section class="box-front" aria-label="Serum box front panel">
  <div class="top-band"></div>
  <div class="brand"><span class="brand-dot"></span>Tidewell Grove</div>
  <h1 class="product-name">Vitamin C<br>Serum</h1>
  <div class="facial-pill">FACIAL SERUM</div>
  <div class="aloe-art" role="img" aria-label="Aloe vera plant illustration"></div>
  <div class="ingredient-box">VITAMIN E &amp;<br>ALOEVERA</div>
  <div class="tagline">Brighter &amp; Healthier Skin</div>
  <div class="lotus-art" role="img" aria-label="Grey lotus flower decoration"></div>
  <div class="volume">2 oz/60ml</div>
</section>

<section class="bottle-label" aria-label="Serum bottle label">
  <div class="brand"><span class="brand-dot"></span>Tidewell Grove</div>
  <h2 class="product-name">Vitamin C<br>Serum</h2>
  <div class="facial-pill">FACIAL SERUM</div>
  <div class="aloe-art" role="img" aria-label="Aloe vera plant illustration"></div>
  <div class="ingredient-box">VITAMIN E &amp;<br>ALOEVERA</div>
  <div class="tagline">Brighter &amp; Healthier Skin</div>
  <div class="lotus-art" role="img" aria-label="Yellow lotus flower decoration"></div>
  <div class="volume">2 oz/60ml</div>
</section>

</body>
</html>
```